Hawaii Luxury Real Estate Sales Broker needs Stationery Design Project

I am a high end property Broker here in Hawaii. I am trying to distinguish myself and my name as a brand as opposed to just being one in hundreds of Realtors out there. I am fortunate to have positioned myself into this particular market and would like to continue to grow my business here by finding the right added touch of classy detail that will make me stand out to Buyers and Sellers of this caliber. I am looking to brand myself via stationary and ads that I can place internationally. The high net worth individuals that I will be reaching out to make this a project that needs to emulate class and sophistication but with a bit of a feminine appeal as I am a woman. :-) Because I live in Hawaii I think this too may be able to play a part of the elegance in design based on the beauty that surrounds us here in the Pacific.

Target Market(s)

High Net Worth Individuals (Carrowell List, Brook Ave Ledger, Private Jet owners)

Industry/Entity Type

Business

Requirements
Must have
• My initials. I would like to see my name or initials always at their fingertips as I want them to be thinking of me as their Realtor.
Should not have
• Nothing too cheesy or touristy. It is important that this is something I can confidently send to high net worth individuals.

```html
<!DOCTYPE html>
<html lang="en">
<head>
<meta charset="utf-8">
<title>Kaia Morrell – Business Card</title>
<link rel="stylesheet" href="https://fonts.googleapis.com/css2?family=Jost:wght@400&family=Open+Sans:wght@400&display=swap">
<style>
  :root {
    --page: #efeeec;
    --card: #ffffff;
    --ink: #0a0a0a;
    --text: #3a3a3a;
    --grey-band: #d6d6d8;
    --grey-mark: #8f8f8f;
    --edge: #cfcfcf;
  }
  html, body {
    margin: 0;
    width: 1200px;
    height: 434px;
    overflow: hidden;
    background: var(--page);
  }
  .stage {
    position: relative;
    width: 1200px;
    height: 434px;
  }
  .card {
    position: absolute;
    top: 71px;
    width: 512px;
    height: 292px;
    background: var(--card);
    border: 1px solid var(--edge);
    overflow: hidden;
    box-sizing: border-box;
  }
  .card--front { left: 58px; }
  .card--back  { left: 630px; }

  /* front */
  .front-band {
    position: absolute;
    top: 0; right: 0;
    width: 150px; height: 100%;
    background: var(--grey-band);
  }
  .brand {
    position: absolute;
    left: 27px;
    display: flex;
    align-items: center;
    gap: 12px;
  }
  .brand--front { top: 138px; }
  .brand__mark {
    width: 18px; height: 18px;
    background: var(--ink);
  }
  .brand__name {
    font-family: "Jost", sans-serif;
    font-weight: 400;
    font-size: 20px;
    letter-spacing: 4px;
    text-transform: uppercase;
    color: var(--ink);
  }
  .address {
    position: absolute;
    left: 27px; top: 186px;
    margin: 0;
    font-family: "Open Sans", sans-serif;
    font-size: 12.5px;
    color: var(--text);
  }
  .contacts {
    position: absolute;
    left: 27px; top: 215px;
    margin: 0; padding: 0;
    list-style: none;
    font-family: "Open Sans", sans-serif;
    font-size: 12.5px;
    color: var(--text);
  }
  .contacts li {
    display: flex;
    align-items: center;
    gap: 6px;
    height: 19px;
  }
  .contacts svg { width: 10px; height: 10px; fill: var(--text); stroke: var(--text); }

  /* back */
  .back-band {
    position: absolute;
    top: 0; left: 0;
    width: 268px; height: 100%;
    background: var(--ink);
  }
  .brand--back {
    left: 330px; top: 236px;
    gap: 8px;
  }
  .brand--back .brand__mark { width: 12px; height: 12px; background: var(--grey-mark); }
  .brand--back .brand__name { font-size: 12px; letter-spacing: 2.5px; color: var(--grey-mark); }
  .back-web {
    position: absolute;
    left: 330px; top: 262px;
    margin: 0;
    font-family: "Open Sans", sans-serif;
    font-size: 12.5px;
    color: var(--text);
  }
</style>
</head>
<body>
<main class="stage">
  <section class="card card--front" aria-label="Card front">
    <div class="front-band"></div>
    <div class="brand brand--front">
      <span class="brand__mark"></span>
      <span class="brand__name">Kaia Morrell</span>
    </div>
    <p class="address">Complex Name, Street Name, Area, City Name,000 000</p>
    <ul class="contacts">
      <li>
        <svg viewBox="0 0 10 10" aria-hidden="true"><circle cx="5" cy="5" r="4.3" fill="none" stroke-width="1"/><path d="M3.3 2.8 L4.2 2.6 L4.6 3.9 L4 4.3 Q4.6 5.6 5.7 6 L6.1 5.4 L7.4 5.8 L7.2 6.7 Q4 7 3.3 2.8 Z" stroke="none"/></svg>
        <span>+1 808 555 0142</span>
      </li>
      <li>
        <svg viewBox="0 0 10 10" aria-hidden="true"><rect x="2.5" y="0.5" width="5" height="9" rx="0.8" fill="none" stroke-width="1"/><rect x="3.5" y="2" width="3" height="3.5" stroke="none"/></svg>
        <span>+1 808 555 0142</span>
      </li>
      <li>
        <svg viewBox="0 0 10 10" aria-hidden="true"><rect x="0.5" y="2.5" width="9" height="5.5" stroke="none"/><path d="M0.5 2.5 L5 5.8 L9.5 2.5" fill="none" stroke="#fff" stroke-width="0.8"/></svg>
        <span>kaia@morrellhomes.com</span>
      </li>
      <li>
        <svg viewBox="0 0 10 10" aria-hidden="true" fill="none" stroke-width="0.9"><circle cx="5" cy="5" r="4.2"/><ellipse cx="5" cy="5" rx="1.8" ry="4.2"/><path d="M0.8 5 H9.2"/></svg>
        <span>www.morrellhomes.com</span>
      </li>
    </ul>
  </section>

  <section class="card card--back" aria-label="Card back">
    <div class="back-band"></div>
    <div class="brand brand--back">
      <span class="brand__mark"></span>
      <span class="brand__name">Kaia Morrell</span>
    </div>
    <p class="back-web">www.morrellhomes.com</p>
  </section>
</main>
</body>
</html>
```